Women's Empowerment & Prayer Brunch - Matching Poster, flyer and Postcard

We are a Christian Event & Travel Company and we are hosting our inaugural event on June 10, 2017. This event is a women's empowerment & prayer brunch aboard a private yacht leaving out of Larkspur Landing, Maryland. The event will cater to women who have a vision to start or have already embarked on the journey of starting or growing a business or ministry. The event calls for a matching poster, flyer and postcard design that give an elegant & exquisite feel with just the right breath of freshness. The colors should reflect our logo as this is our launch event. I have also included 2 photos of the Coralwind Heritage Village production (one of our sponsors) - Please include but do not make it take over the design - this is to advertise the door prize. The final design will portray the branding of the company (Christian, travel, events, elegance, professional), the branding of the event (elegant and luxurious) and the importance of this launch event.
Please include the following information:
Brightwell Event & Travel Group presents
Event name: Climbing the Hill: Trust, Service & Devotion.
Tag Line/Description: An Exquisite Women's Empowerment & Prayer Brunch.
Guest Speaker: Minister Harriet L. Dunmore (Photo included)
VP of TrustLine
Asst. Pastor & First Lady of Gilead Baptist Church
Special Guest Psalmist: Minister Tessa Holbrook (Photo Included)
Worship Director of Stonefield Community Church
Vocalist, Songwriter, Musician, and Clinician
Venue: Aboard the Regal Tide Yacht
Dock: Larkspur Landing
342 Marlow Court, Oxen Hill, MD 20712
Boarding 10:00am
Sailing Promptly at 10:30am
(Please be on time the yacht will not wait)
Date: Saturday June 10, 2017
Tickets: Early Bird US$75.00/person (ends May 15, 2017)
Regular Tickets US$95.99
Purchase Tickets at www.brightwellevent-travel.example/climbing-the-hill
SPACE IS LIMITED DUE TO YACHT CAPACITY
Grand Prize: Julian Ardent Purse
Door Prize: 2 Tickets to the Islander Coralwind Heritage Village
Other prizes for special ladies in attendance.
Ladies are asked to dress in Elegant White Ensemble
Corporate Sponsors:
The Coralwind Heritage Village (Logo included)
R. Lanning Photography (Logo included)
Special Thanks to our Individual Sponsors:
Mrs. G. Whitlow, Mr. K Prentice & Mr. S. Dorsey

Target Market(s)

Women, Business, Ministry, Christians, Middle to Upper Class

Industry/Entity Type

Events

Font styles to use
Serif
Script

Requirements
Must have
• Elegance, professional, vivid in color & font. be creative in Visual and FONT!
• Poster: 18" X 24"
• Flyer: one sided.
• ***** the final design chosen will have a cross referenced design of 1 flyer, 1 postcard 1 poster. This was included so you have a reference - Be creative!!!!!!
Nice to have
• Matching across all 3 designs (poster, flyer & postcard) but sized appropriately and just enough difference to play up the design and be appealing.
• I uploaded 3 example flyers to give you inspiration of the type of visuals I'm looking for. I removed my amateur sample because the designs were copying it instead of being creative.
Should not have
• Any thing inappropriate, alcohol oriented or sexual

```html
<!DOCTYPE html>
<html lang="en">
<head>
<meta charset="utf-8">
<title>Climbing the Hill – Women's Empowerment &amp; Prayer Brunch</title>
<link rel="stylesheet" href="https://fonts.googleapis.com/css2?family=Pinyon+Script&family=Playfair+Display:ital,wght@0,400;0,700;1,400;1,700&family=Raleway:wght@400;600;700&family=Michroma&display=swap">
<style>
:root{
  --navy-top:#1168c0;
  --sky-mid:#3d8fd6;
  --sky-low:#a9cde6;
  --sea:#9cc3c8;
  --sea-deep:#86b3ba;
  --gold:#f2c230;
  --gold-deep:#c99a1c;
  --white:#ffffff;
  --link:#1a4fa6;
  --ink-soft:#f4f8fc;
}
*{margin:0;padding:0;box-sizing:border-box}
html,body{width:900px;height:1200px;overflow:hidden}
body{font-family:"Raleway",sans-serif;color:var(--white)}
.poster{position:relative;width:900px;height:1200px;overflow:hidden}
.backdrop{position:absolute;inset:0;
  background:linear-gradient(180deg,var(--navy-top) 0,var(--navy-top) 257px,#2a84d0 300px,var(--sky-mid) 520px,#7fb6e0 760px,var(--sky-low) 880px,#c6dde8 888px,var(--sea) 892px,#a9c9cb 1000px,var(--sea-deep) 1200px)}
.abs{position:absolute}
.brand{left:0;right:0;top:70px;text-align:center;font-family:"Playfair Display",serif;font-size:20px;color:var(--gold);display:flex;justify-content:center;align-items:center;gap:10px}
.brand-dot{width:14px;height:14px;border-radius:50%;background:var(--gold)}
.presents{left:0;right:0;top:133px;text-align:center;font-family:"Playfair Display",serif;font-style:italic;font-weight:700;font-size:15px;letter-spacing:1px}
.title{left:0;right:0;top:136px;text-align:center;font-family:"Pinyon Script",cursive;font-size:96px;line-height:1.1;white-space:nowrap}
.band{left:0;right:0;top:257px;height:46px;border-top:2px solid var(--ink-soft);border-bottom:2px solid var(--ink-soft);display:flex;align-items:center;justify-content:center}
.theme{font-family:"Michroma",sans-serif;color:var(--gold);font-size:19px;letter-spacing:6px}
.tagline{left:0;right:0;top:315px;text-align:center;font-size:15px;font-variant:small-caps;letter-spacing:3px;font-weight:600}
.date{left:0;right:0;top:340px;text-align:center;font-family:"Michroma",sans-serif;color:var(--gold);font-size:24px;letter-spacing:5px}
.portrait{width:146px;height:188px;border-radius:50%;border:5px solid var(--gold);box-shadow:0 0 0 2px var(--gold-deep)}
.portrait.speaker{left:272px;top:394px;background:radial-gradient(ellipse at 50% 55%,#8a3a36 0,#b42a2a 40%,#6e4336 75%)}
.portrait.guest{left:482px;top:394px;background:radial-gradient(ellipse at 50% 45%,#6b4a3a 0,#2b2a2e 55%,#1e2430 100%)}
.role{font-family:"Playfair Display",serif;font-style:italic;font-weight:700;font-size:20px}
.bio{font-size:15px;line-height:1.25;letter-spacing:.5px}
.bio b{font-weight:700;font-size:16px;letter-spacing:1px}
.bio p{margin-top:6px}
.left-bio{right:644px;top:406px;text-align:right;width:260px}
.right-bio{left:645px;top:404px;width:250px}
.divider{width:2px;background:var(--ink-soft);top:600px;height:165px}
.col-head{font-family:"Playfair Display",serif;font-style:italic;font-weight:700;font-size:19px;letter-spacing:1px}
.col-text{font-size:15px;line-height:1.35;letter-spacing:1px}
.note{font-family:"Playfair Display",serif;font-style:italic;font-weight:700;font-size:17px;line-height:1.25;letter-spacing:1px}
.dock{right:597px;top:607px;text-align:right}
.boarding{left:325px;width:250px;top:605px;text-align:center}
.tickets{left:597px;top:607px;width:280px}
.tickets b{font-weight:700}
.tickets .ends{font-family:"Playfair Display",serif;font-style:italic;font-weight:700;font-size:14px;display:block;text-align:right;padding-right:55px}
.buy{left:0;right:0;top:783px;text-align:center}
.url{font-size:17px;color:var(--link);letter-spacing:.6px;margin-top:2px}
.rule{height:2px;background:var(--ink-soft)}
.capacity{left:0;right:0;top:858px;text-align:center;font-weight:700;font-size:18px;letter-spacing:2px}
.badge{width:84px;height:72px;border-radius:50%;background:var(--white);border:4px solid var(--gold);box-shadow:0 0 0 2px var(--gold-deep);display:flex;align-items:center;justify-content:center;text-align:center}
.badge span{font-family:"Michroma",sans-serif;font-size:13px;color:var(--gold-deep);letter-spacing:2px;line-height:1.25;transform:rotate(-14deg)}
.prize-big{font-family:"Playfair Display",serif;font-style:italic;font-weight:700;font-size:24px;line-height:1.25;letter-spacing:1.5px}
.prize-small{font-family:"Playfair Display",serif;font-style:italic;font-weight:700;font-size:15px;line-height:1.3;letter-spacing:1px}
.other{left:0;right:0;top:988px;text-align:center;font-family:"Playfair Display",serif;font-style:italic;font-size:15px;letter-spacing:1px}
.sponsor-label{left:164px;top:1050px;font-family:"Michroma",sans-serif;font-size:18px;letter-spacing:4px;line-height:1.75;color:transparent;-webkit-text-stroke:1px var(--gold)}
.sponsor-box{top:1040px;height:74px;display:flex;align-items:center;justify-content:center;text-align:center;font-family:"Playfair Display",serif;font-size:13px;color:#7a5a1a;padding:6px}
.sponsor-box.photo{left:376px;width:103px;background:#f1ede8}
.sponsor-box.village{left:514px;width:212px;background:var(--white);font-size:18px;font-weight:700}
.thanks{left:0;right:0;top:1127px;text-align:center;font-family:"Playfair Display",serif;font-style:italic;font-weight:700;font-size:15px;letter-spacing:1px}
.patrons{left:0;right:0;top:1148px;text-align:center;font-size:20px;letter-spacing:1.5px;color:var(--ink-soft)}
</style>
</head>
<body>
<main class="poster">
  <div class="backdrop" role="img" aria-label="Clear blue sky meeting a calm turquoise sea at the horizon"></div>

  <div class="abs brand"><span class="brand-dot"></span>Brightwell Event &amp; Travel Group</div>
  <div class="abs presents">presents</div>
  <h1 class="abs title">Climbing the Hill</h1>

  <div class="abs band"><span class="theme">TRUST, SERVICE &amp; DEVOTION</span></div>
  <div class="abs tagline">An Exquisite Women's Empowerment &amp; Prayer Brunch</div>
  <div class="abs date">SATURDAY, JUNE 10, 2017</div>

  <section class="abs left-bio">
    <div class="role">Guest Speaker</div>
    <div class="bio" style="margin-top:10px">Minister<br><b>Harriet L. Dunmore</b>
      <p>VP of TrustLine</p>
      <p style="margin-top:20px">Asst. Pastor &amp; First Lady of<br>Gilead Baptist Church</p>
    </div>
  </section>
  <div class="abs portrait speaker" role="img" aria-label="Portrait photo of guest speaker Minister Harriet L. Dunmore"></div>
  <div class="abs portrait guest" role="img" aria-label="Portrait photo of special guest Minister Tessa Holbrook"></div>
  <section class="abs right-bio">
    <div class="role">Special Guest</div>
    <div class="bio" style="margin-top:10px">Minister<br><b>Tessa Holbrook</b>
      <p>Worship Director of<br>Stonefield Community Church</p>
      <p style="margin-top:14px">Vocalist, Songwriter,<br>Musician, and Clinician</p>
    </div>
  </section>

  <div class="abs divider" style="left:318px"></div>
  <div class="abs divider" style="left:581px"></div>

  <section class="abs dock">
    <div class="col-head">Dock:</div>
    <div class="col-text" style="margin-top:8px">Larkspur Landing<br>342 Marlow Court<br>Oxen Hill, MD 20712</div>
    <div class="note" style="margin-top:12px">Ladies are asked to dress<br>in Elegant White Ensemble</div>
  </section>
  <section class="abs boarding">
    <div class="col-head">Boarding:</div>
    <div class="col-text">10:00am</div>
    <div class="col-head" style="margin-top:8px">Sailing Promptly at:</div>
    <div class="col-text">10:30am</div>
    <div class="note" style="margin-top:10px">(Please be on time,<br>the yacht will not wait)</div>
  </section>
  <section class="abs tickets">
    <div class="col-head">Tickets:</div>
    <div class="col-text" style="margin-top:8px"><b>Early Bird:</b><br>US$75.00/person</div>
    <span class="ends">(ends May 15, 2017)</span>
    <div class="col-text" style="margin-top:10px"><b>Regular Tickets:</b><br>US$95.99</div>
  </section>

  <section class="abs buy">
    <div class="col-head">Purchase Tickets at:</div>
    <div class="url">www.brightwellevent-travel.example/climbing-the-hill</div>
  </section>
  <div class="abs rule" style="left:305px;width:300px;top:845px"></div>
  <div class="abs capacity">SPACE IS LIMITED DUE TO YACHT CAPACITY</div>

  <div class="abs badge" style="left:152px;top:899px"><span>GRAND<br>PRIZE</span></div>
  <div class="abs prize-big" style="left:257px;top:906px">Julian Ardent<br>Purse</div>
  <div class="abs badge" style="left:512px;top:899px"><span>DOOR<br>PRIZE</span></div>
  <div class="abs prize-small" style="left:618px;top:905px">2 Tickets<br>to the Islander Coralwind<br>Heritage Village</div>
  <div class="abs other">Other prizes for special ladies in attendance.</div>
  <div class="abs rule" style="left:293px;width:314px;top:1020px"></div>

  <div class="abs sponsor-label">CORPORATE<br>SPONSORS</div>
  <div class="abs sponsor-box photo">R. Lanning Photography</div>
  <div class="abs sponsor-box village">Coralwind Heritage Village</div>

  <div class="abs thanks">Special Thanks to our Individual Sponsors:</div>
  <div class="abs patrons">Mrs. G. Whitlow, Mr. K Prentice &amp; Mr. S. Dorsey</div>
</main>
</body>
</html>
```